eCommerce website for the sale of vehicle tyres

We need the design of a logo and website for an ecommerce website that sells tyres to vehicle owners.

Users to the website should be able to search brand of tyre, type of tyre and make payment online.

The website should have algorithm to calculate delivery price based on user location and include in total price payable by CoinLark or SwiftTill.

Multi-language website (5 languages)
Content for website available in attached brief.

Number of pages:
1. Home page (with slider on how it works and search area)
2. Search results page
3. About Us page
4. Contact Us page

Target Market(s)

Owners of vehicles

Industry/Entity Type

Automotive

Logo Text

Vorel

Coding

Coded - Design and coding required

Number of Pages Required

5+ page

Font styles to use
Serif

Colors
0255a3
9d9d9d
ec1f27

Requirements
Must have
• Clean design
• Search feature on front page
Should not have
• Complicated

```html
<!DOCTYPE html>
<html lang="en">
<head>
<meta charset="utf-8">
<title>Vorel – Tyres Online</title>
<link href="https://fonts.googleapis.com/css2?family=Montserrat:wght@400;600;700&family=Open+Sans:wght@400;600;700&display=swap" rel="stylesheet">
<style>
:root{
  --blue:#0255a3;
  --blue-dark:#01407b;
  --blue-deep:#013366;
  --red:#ec1f27;
  --grey:#9d9d9d;
  --grey-light:#ececec;
  --grey-card:#d9d9d9;
  --ink:#1d1f22;
  --caption:#2a2c30;
  --white:#ffffff;
}
*{box-sizing:border-box;margin:0;padding:0}
html,body{width:1200px;height:2252px;overflow:hidden}
body{font-family:"Open Sans",Arial,sans-serif;color:var(--ink);background:var(--white);position:relative}
ul{list-style:none}

/* hero */
.hero{position:absolute;left:0;top:0;width:1200px;height:620px;
  background:linear-gradient(180deg,#2b2e33 0%,#1a1c20 55%,#0e0f12 100%)}
.hero-photo{position:absolute;inset:0;background:radial-gradient(ellipse at 50% 35%,rgba(120,125,135,.35),rgba(0,0,0,0) 60%)}
.logo{position:absolute;left:72px;top:18px;display:flex;align-items:center;gap:10px;
  font-family:"Montserrat",sans-serif;font-weight:700;font-size:40px;color:var(--white);letter-spacing:.5px}
.logo-mark{width:12px;height:12px;background:var(--red)}
.top-links{position:absolute;right:72px;top:10px;display:flex;gap:22px;font-size:13px;color:#d6d6d6}
.top-links li{display:flex;align-items:center;gap:6px}
.top-links svg{width:12px;height:12px}

.main-nav{position:absolute;left:40px;top:134px;width:1120px;height:46px;background:var(--blue);
  display:flex;align-items:center;border-bottom:3px solid var(--blue-deep)}
.main-nav ul{display:flex;height:100%}
.main-nav li{display:flex;align-items:center;padding:0 26px;font-family:"Montserrat",sans-serif;
  font-size:13px;font-weight:600;color:var(--white);letter-spacing:.5px}
.main-nav li.active{background:var(--blue-deep);margin-left:24px;padding:0 22px}
.cart{margin-left:auto;margin-right:26px;display:flex;align-items:center;gap:14px;color:var(--white);font-size:13px}
.cart svg{width:20px;height:20px}

.search-title{position:absolute;top:322px;width:100%;text-align:center;font-family:"Montserrat",sans-serif;
  font-weight:700;font-size:34px;letter-spacing:2px;color:var(--white)}
.search-bar{position:absolute;left:240px;top:428px;width:736px;height:60px;background:var(--white);
  display:flex;align-items:center;padding-left:12px;gap:12px}
.search-select{width:150px;height:36px;border:1px solid #cfcfcf;display:flex;align-items:center;
  justify-content:space-between;padding:0 10px;font-size:12px;color:#777}
.search-btn{margin-left:auto;width:60px;height:60px;background:var(--blue);display:flex;align-items:center;justify-content:center}

/* promo banner */
.promo{position:absolute;left:72px;top:712px;width:1056px;height:224px;display:flex;background:var(--grey-light)}
.promo-half{position:relative;width:528px;height:224px;padding:56px 0 0 24px}
.promo-summer{background:linear-gradient(90deg,#f1f1f1,#e3e3e3)}
.promo-winter{background:var(--blue)}
.promo h3{font-family:"Montserrat",sans-serif;font-size:34px;font-weight:700;color:var(--blue)}
.promo-winter h3{color:var(--white)}
.promo p{width:230px;margin-top:6px;font-size:12px;line-height:1.4;color:#555}
.promo-winter p{color:#dbe6f3}
.promo .shop{display:block;margin-top:12px;font-size:12px;font-weight:700;color:var(--blue)}
.promo-winter .shop{color:var(--white)}
.promo-art{position:absolute;right:24px;top:14px;width:200px;height:196px;border-radius:50%}
.promo-summer .promo-art{background:radial-gradient(circle,#1a5fb0 0%,#0b2d57 55%,#111 75%)}
.promo-winter .promo-art{background:radial-gradient(circle,#8a8d92 0%,#2a2c30 45%,#0c0d0f 75%)}

/* products */
.section-title{position:absolute;top:992px;width:100%;text-align:center;font-family:"Montserrat",sans-serif;
  font-weight:700;font-size:34px;color:var(--blue)}
.tabs{position:absolute;left:240px;top:1072px;width:720px;height:68px;display:flex;border-bottom:1px solid #e2e2e2}
.tabs li{flex:1;display:flex;align-items:center;justify-content:center;font-family:"Montserrat",sans-serif;
  font-size:14px;font-weight:600;color:#444;position:relative}
.tabs li.active{background:var(--blue);color:var(--white)}
.tabs li.active::after{content:"";position:absolute;bottom:-12px;left:50%;margin-left:-12px;
  border-left:12px solid transparent;border-right:12px solid transparent;border-top:12px solid var(--blue)}
.products{position:absolute;left:0;top:1140px;width:1200px;height:780px;background:var(--grey-light)}
.grid{position:absolute;left:84px;top:48px;display:grid;grid-template-columns:repeat(4,240px);gap:40px 24px}
.card{width:240px;background:var(--caption)}
.card-img{height:196px;background:var(--grey-card);display:flex;align-items:center;justify-content:center}
.card-img span{width:150px;height:150px;border-radius:50%;
  background:radial-gradient(circle,#9a9da2 0%,#3b3d41 40%,#141518 70%)}
.card-body{padding:14px 16px 16px;text-align:center;color:var(--white)}
.card-name{font-size:11px;font-weight:600;line-height:1.4;letter-spacing:.3px}
.card-price{margin-top:8px;font-family:"Montserrat",sans-serif;font-size:20px;font-weight:700}
.card.featured{background:var(--blue)}
.card.featured .card-body{background:var(--blue)}
.add-cart{display:inline-block;margin-top:12px;padding:9px 18px;border:1px solid var(--white);
  background:var(--white);color:var(--blue);font-size:12px;font-weight:700;letter-spacing:.5px}

/* footer */
.footer{position:absolute;left:0;top:1920px;width:1200px;height:264px;background:var(--blue);color:var(--white)}
.footer-cols{position:absolute;left:84px;top:40px;display:flex;gap:0}
.footer-col{width:206px}
.footer-col h4{font-family:"Montserrat",sans-serif;font-size:14px;font-weight:700;margin-bottom:14px}
.footer-col li{font-size:12px;line-height:24px;color:#d7e3f1}
.footer-col li::before{content:"•";margin-right:8px}
.social{display:flex;gap:12px}
.social span{width:36px;height:36px;background:var(--red)}
.footer-bar{position:absolute;left:0;top:2184px;width:1200px;height:68px;background:var(--blue-deep);
  display:flex;align-items:center;padding:0 84px;color:var(--white);font-size:12px}
.feature{display:flex;align-items:center;gap:10px;margin-right:56px;line-height:1.3;font-weight:700;font-size:11px}
.feature svg{width:28px;height:28px}
.copyright{margin-left:auto;font-size:11px;color:#c8d6e8}
</style>
</head>
<body>

<header class="hero">
  <div class="hero-photo" role="img" aria-label="Dark photo of stacked alloy wheels and tyres"></div>
  <div class="logo"><span>Vorel</span><span class="logo-mark"></span></div>
  <ul class="top-links">
    <li><svg viewBox="0 0 12 12"><circle cx="6" cy="4" r="3" fill="#d6d6d6"/><rect x="1" y="8" width="10" height="4" rx="2" fill="#d6d6d6"/></svg>Login</li>
    <li><svg viewBox="0 0 12 12"><circle cx="6" cy="4" r="3" fill="#d6d6d6"/><rect x="1" y="8" width="10" height="4" rx="2" fill="#d6d6d6"/></svg>My account</li>
    <li><svg viewBox="0 0 12 12"><path d="M1 2h2l2 6h6l1-4H4" stroke="#d6d6d6" fill="none" stroke-width="1.4"/></svg>Checkout</li>
    <li><svg viewBox="0 0 12 12"><rect x="0" y="2" width="12" height="8" fill="#c33"/><rect x="0" y="5" width="12" height="2" fill="#fff"/></svg>English ▾</li>
    <li>USD ▾</li>
  </ul>
  <nav class="main-nav">
    <ul>
      <li class="active">HOME</li>
      <li>CAR TYRES</li>
      <li>BIKE TYRES</li>
      <li>ALLOY WHEELS</li>
      <li>ABOUT US</li>
      <li>CONTACT US</li>
    </ul>
    <div class="cart">
      <svg viewBox="0 0 20 20"><path d="M1 3h3l3 10h9l2-7H6" stroke="#fff" fill="none" stroke-width="2"/><circle cx="8" cy="17" r="1.6" fill="#fff"/><circle cx="15" cy="17" r="1.6" fill="#fff"/></svg>
      <span>$0.00</span><span>0 items</span>
    </div>
  </nav>
  <h1 class="search-title">SEARCH TYRE SIZE</h1>
  <div class="search-bar">
    <div class="search-select">Width (Ex.) <span>▾</span></div>
    <div class="search-select">Profile (Ex.) <span>▾</span></div>
    <div class="search-select">Size (Ex.) <span>▾</span></div>
    <div class="search-select">Speed (Ex.) <span>▾</span></div>
    <div class="search-btn"><svg width="24" height="24" viewBox="0 0 24 24"><circle cx="10" cy="10" r="7" stroke="#fff" stroke-width="3" fill="none"/><path d="M15 15l7 7" stroke="#fff" stroke-width="3"/></svg></div>
  </div>
</header>

<section class="promo">
  <div class="promo-half promo-summer">
    <h3>Summer Tyres</h3>
    <p>Lorem ipsum dolor sit amet conse ctetur adipiscing elit, sed do eiusmod.</p>
    <span class="shop">SHOP NOW</span>
    <div class="promo-art" role="img" aria-label="Blue alloy wheel with tyre"></div>
  </div>
  <div class="promo-half promo-winter">
    <h3>Winter Tyres</h3>
    <p>Lorem ipsum dolor sit amet conse ctetur adipiscing elit, sed do eiusmod.</p>
    <span class="shop">SHOP NOW</span>
    <div class="promo-art" role="img" aria-label="Winter tyre on dark alloy wheel"></div>
  </div>
</section>

<h2 class="section-title">OUR PRODUCTS</h2>
<ul class="tabs">
  <li>POPULAR</li>
  <li class="active">NEW ARRIVALS</li>
  <li>BEST SELLERS</li>
</ul>

<section class="products">
  <div class="grid">
    <article class="card featured">
      <div class="card-img"><span role="img" aria-label="Tyre on black alloy wheel"></span></div>
      <div class="card-body"><p class="card-name">KELD STRATA SPORT RIM SILVER WITH GLOSS FINISH</p><p class="card-price">$20.96</p><span class="add-cart">ADD TO CART</span></div>
    </article>
    <article class="card">
      <div class="card-img"><span role="img" aria-label="Silver alloy wheel"></span></div>
      <div class="card-body"><p class="card-name">KELD STRATA SPORT RIM SILVER WITH GLOSS FINISH</p><p class="card-price">$20.96</p></div>
    </article>
    <article class="card">
      <div class="card-img"><span role="img" aria-label="Single tyre"></span></div>
      <div class="card-body"><p class="card-name">KELD STRATA SPORT RIM SILVER WITH GLOSS FINISH</p><p class="card-price">$20.96</p></div>
    </article>
    <article class="card">
      <div class="card-img"><span role="img" aria-label="Tyre on chrome wheel"></span></div>
      <div class="card-body"><p class="card-name">KELD STRATA SPORT RIM SILVER WITH GLOSS FINISH</p><p class="card-price">$20.96</p></div>
    </article>
    <article class="card">
      <div class="card-img"><span role="img" aria-label="Tyre on dark alloy wheel"></span></div>
      <div class="card-body"><p class="card-name">KELD STRATA SPORT RIM SILVER WITH GLOSS FINISH</p><p class="card-price">$20.96</p></div>
    </article>
    <article class="card">
      <div class="card-img"><span role="img" aria-label="Tyre tread close-up"></span></div>
      <div class="card-body"><p class="card-name">KELD STRATA SPORT RIM SILVER WITH GLOSS FINISH</p><p class="card-price">$20.96</p></div>
    </article>
    <article class="card">
      <div class="card-img"><span role="img" aria-label="Pair of tyres on wheels"></span></div>
      <div class="card-body"><p class="card-name">KELD STRATA SPORT RIM SILVER WITH GLOSS FINISH</p><p class="card-price">$20.96</p></div>
    </article>
    <article class="card">
      <div class="card-img"><span role="img" aria-label="Pair of tyres on alloy wheels"></span></div>
      <div class="card-body"><p class="card-name">KELD STRATA SPORT RIM SILVER WITH GLOSS FINISH</p><p class="card-price">$20.96</p></div>
    </article>
  </div>
</section>

<footer class="footer">
  <div class="footer-cols">
    <div class="footer-col"><h4>MAIN MENU</h4><ul><li>Home</li><li>What's New</li><li>Featured</li><li>Top sellers</li></ul></div>
    <div class="footer-col"><h4>EXTRAS</h4><ul><li>Specials</li><li>Brands</li><li>Reviews</li></ul></div>
    <div class="footer-col"><h4>INFORMATION</h4><ul><li>Privacy Policy</li><li>Contacts</li><li>Terms &amp; Conditions</li></ul></div>
    <div class="footer-col"><h4>YOUR ACCOUNT</h4><ul><li>Shipping &amp; Returns</li><li>Advanced Search</li><li>Create an Account</li><li>Log In</li></ul></div>
    <div class="footer-col"><h4>FOLLOW US ON</h4><div class="social"><span></span><span></span><span></span></div></div>
  </div>
</footer>
<div class="footer-bar">
  <div class="feature"><svg viewBox="0 0 28 28"><circle cx="14" cy="14" r="12" stroke="#fff" stroke-width="2" fill="none"/><path d="M8 14l4 4 8-8" stroke="#fff" stroke-width="2" fill="none"/></svg><span>SATISFACTION<br>100% GUARANTEED</span></div>
  <div class="feature"><svg viewBox="0 0 28 28"><rect x="2" y="8" width="14" height="11" stroke="#fff" stroke-width="2" fill="none"/><path d="M16 12h5l4 4v3h-9" stroke="#fff" stroke-width="2" fill="none"/><circle cx="7" cy="21" r="2" fill="#fff"/><circle cx="21" cy="21" r="2" fill="#fff"/></svg><span>FREE SHIPPING<br>ON ORDERS OVER $99</span></div>
  <div class="feature"><svg viewBox="0 0 28 28"><path d="M22 14a8 8 0 1 1-3-6.2" stroke="#fff" stroke-width="2" fill="none"/><path d="M19 3v5h5" stroke="#fff" stroke-width="2" fill="none"/></svg><span>7 DAY<br>EASY RETURN</span></div>
  <p class="copyright">Copyright © 2016 Vorel. All Rights Reserved</p>
</div>

</body>
</html>
```